We are Harwell Heart and Circulatory Care and located at 2945 Pelton Avenue, Suites 300 & 400, Larkfield, VA 22784. Our phone is 540-318-4971 We are creating a brochure to promote our Arrhythmia Clinic. Our audience is both patients and referring to help education and understand our arrhythmias. Please add imaging. We appreciate any create suggestions when comes to imaging as long as relates to medical information being provided.

```html
<!DOCTYPE html>
<html lang="en">
<head>
<meta charset="utf-8">
<title>Harwell Heart and Circulatory Care – Arrhythmia Clinic Brochure</title>
<link href="https://fonts.googleapis.com/css2?family=Montserrat:wght@500;600;700&family=Open+Sans:wght@400;600&display=swap" rel="stylesheet">
<style>
:root{
  --backdrop:#7f939b;
  --cover:#2f3a40;
  --cover-deep:#262f34;
  --white:#ffffff;
  --page:#f5f5f3;
  --page-shade:#ececea;
  --teal:#2a6a84;
  --teal-dark:#24586d;
  --ink:#3a3f44;
  --muted:#5d6469;
  --panel:#e2e3e4;
}
*{box-sizing:border-box;margin:0;padding:0}
html,body{width:1200px;height:2240px;overflow:hidden}
body{background:var(--backdrop);font-family:"Open Sans",Arial,sans-serif;position:relative}
.scene{position:absolute;left:0;width:1200px;height:746px}
.abs{position:absolute}

/* Front cover */
.front-cover{left:172px;top:40px;width:400px;height:285px;background:linear-gradient(135deg,var(--cover) 0%,var(--cover-deep) 100%);overflow:hidden}
.tag{position:absolute;border:1px solid var(--white);color:var(--white);font-family:"Montserrat",Arial,sans-serif;font-weight:600;letter-spacing:.04em;display:flex;align-items:center;justify-content:center}
.front-cover .tag{left:21px;top:63px;width:127px;height:22px;font-size:12px}
.cover-title{position:absolute;left:21px;top:106px;font-family:"Montserrat",Arial,sans-serif;font-weight:700;font-size:18.5px;line-height:20px;color:var(--white);letter-spacing:.02em;text-transform:uppercase;z-index:2}
.cover-rule{position:absolute;left:21px;top:185px;width:52px;height:2px;background:var(--white)}
.cover-web{position:absolute;left:21px;top:205px;font-family:"Montserrat",Arial,sans-serif;font-weight:600;font-size:10px;letter-spacing:.12em;color:var(--white)}
.cover-art{position:absolute;left:210px;top:40px;width:190px;height:220px;background:radial-gradient(ellipse at 50% 50%,#d45aa0 0%,#5aa6e6 26%,#2d6fae 48%,rgba(47,58,64,0) 70%)}

/* Back cover */
.back-cover{left:615px;top:43px;width:405px;height:285px;background:linear-gradient(135deg,var(--cover) 0%,var(--cover-deep) 100%)}
.back-cover .tag{left:17px;top:163px;width:96px;height:18px;font-size:10px}
.contact-title{position:absolute;left:17px;top:189px;font-family:"Montserrat",Arial,sans-serif;font-weight:600;font-size:13px;color:var(--white)}
.contact-rule{position:absolute;left:17px;top:208px;width:40px;height:1px;background:var(--white)}
.contact-row{position:absolute;left:17px;display:flex;gap:6px;align-items:flex-start;font-family:"Montserrat",Arial,sans-serif;font-weight:600;font-size:7px;line-height:8px;color:var(--white)}
.contact-row svg{width:9px;height:9px;flex:none}

/* Spreads */
.spread{left:198px;top:354px;width:792px;height:290px;display:flex;box-shadow:0 2px 6px rgba(0,0,0,.15)}
.page{position:relative;width:396px;height:290px;background:var(--page);overflow:hidden}
.page.left{background:linear-gradient(90deg,var(--page) 85%,var(--page-shade) 100%)}
.page.right{background:linear-gradient(90deg,var(--page-shade) 0%,var(--page) 12%)}
.page-heading{position:absolute;left:0;right:0;text-align:center;font-family:"Montserrat",Arial,sans-serif;font-weight:700;color:var(--teal)}
.heading-rule{position:absolute;height:1.5px;background:var(--teal-dark)}
.photo{position:absolute;border:1px solid #2b3338}
.panel{position:absolute;background:var(--panel)}
.panel-title{font-family:"Montserrat",Arial,sans-serif;font-weight:600;color:var(--teal)}
.small{font-size:6.5px;line-height:8px;color:var(--muted)}
.item{position:absolute;display:flex;gap:5px;width:188px}
.item svg{width:7px;height:7px;flex:none;margin-top:1px}
.item-title{font-family:"Montserrat",Arial,sans-serif;font-weight:600;font-size:7.5px;color:var(--teal)}
.item .small{font-size:5.5px;line-height:6.5px}
.caption{position:absolute;text-align:center}
.caption-title{font-family:"Montserrat",Arial,sans-serif;font-weight:600;font-size:9px;color:var(--teal);margin-bottom:2px}
.caption .small{font-size:6px;line-height:7.5px}
.symptom{position:absolute;left:12px;display:flex;align-items:center;gap:8px;font-size:7.5px;font-weight:600;color:var(--ink)}
.symptom span.dot{width:14px;height:14px;border-radius:50%;background:#5a7f93;flex:none}
.life-item{position:absolute;left:17px;display:flex;gap:7px;font-size:6px;line-height:7px;color:var(--ink);width:170px}
.life-item svg{width:6px;height:6px;flex:none}
</style>
</head>
<body>
<svg width="0" height="0" style="position:absolute">
  <symbol id="tick" viewBox="0 0 10 10"><circle cx="5" cy="5" r="5" fill="#2a6a84"/><path d="M2.6 5.2 4.3 6.8 7.4 3.5" fill="none" stroke="#fff" stroke-width="1.3"/></symbol>
  <symbol id="phone" viewBox="0 0 10 10"><path d="M2 1h2l1 2.5-1.3.8a5.5 5.5 0 0 0 2 2l.8-1.3L9 6v2a1 1 0 0 1-1 1A7.5 7.5 0 0 1 1 2a1 1 0 0 1 1-1z" fill="#fff"/></symbol>
  <symbol id="globe" viewBox="0 0 10 10"><circle cx="5" cy="5" r="4.2" fill="none" stroke="#fff"/><ellipse cx="5" cy="5" rx="1.8" ry="4.2" fill="none" stroke="#fff" stroke-width=".8"/><path d="M1 5h8" stroke="#fff" stroke-width=".8"/></symbol>
  <symbol id="pin" viewBox="0 0 10 10"><path d="M5 .5a3.2 3.2 0 0 1 3.2 3.2C8.2 6.2 5 9.5 5 9.5S1.8 6.2 1.8 3.7A3.2 3.2 0 0 1 5 .5z" fill="#fff"/><circle cx="5" cy="3.7" r="1.2" fill="#2f3a40"/></symbol>
</svg>

<!-- Scene 1 -->
<section class="scene" style="top:0">
  <div class="abs front-cover">
    <div class="cover-art" role="img" aria-label="Glowing blue digital heart with a heartbeat trace"></div>
    <div class="tag">ARRHYTHMIAS</div>
    <h1 class="cover-title">Harwell Heart<br>and Circulatory<br>Care</h1>
    <div class="cover-rule"></div>
    <div class="cover-web">www.harwellrhythm.com</div>
  </div>
  <div class="abs back-cover">
    <div class="tag">ARRHYTHMIAS</div>
    <div class="contact-title">Contact us</div>
    <div class="contact-rule"></div>
    <div class="contact-row" style="top:221px"><svg><use href="#phone"/></svg>540-318-4971</div>
    <div class="contact-row" style="top:236px"><svg><use href="#globe"/></svg>www.harwellrhythm.com</div>
    <div class="contact-row" style="top:250px"><svg><use href="#pin"/></svg>2945 Pelton Avenue, Suites 300 &amp; 400,<br>Larkfield, VA 22784</div>
  </div>
  <div class="abs spread">
    <div class="page left">
      <div class="page-heading" style="top:17px;font-size:12px;letter-spacing:.04em">ARRHYTHMIAS</div>
      <div class="panel" style="left:30px;top:46px;width:150px;height:78px;padding:10px 12px">
        <div class="panel-title" style="font-size:11px;margin-bottom:2px">About Arrhythmias</div>
        <p style="font-size:7.5px;line-height:9.5px;color:var(--muted)">Arrhythmias are disorders of the electrical system of the heart. A common arrhythmia is atrial fibrillation.</p>
      </div>
      <div class="photo" role="img" aria-label="Patient clutching chest beside an ECG trace" style="left:176px;top:43px;width:202px;height:86px;background:linear-gradient(90deg,#1c4a73 0%,#2f5f8c 45%,#b8232b 75%,#d8343a 100%)"></div>
      <div class="photo" role="img" aria-label="Illustrated heart with electrical signals" style="left:32px;top:142px;width:123px;height:71px;background:linear-gradient(90deg,#c94050 0%,#6a86a8 60%,#2b5a86 100%)"></div>
      <div class="photo" role="img" aria-label="Heart monitor screen showing a pulse line" style="left:158px;top:142px;width:103px;height:71px;background:linear-gradient(180deg,#123838 0%,#0d2222 100%)"></div>
      <div class="photo" role="img" aria-label="Red heart model with a stethoscope" style="left:267px;top:140px;width:111px;height:64px;background:linear-gradient(135deg,#f0e6dd 0%,#e3d2c6 55%,#c92f35 100%)"></div>
      <div class="caption" style="left:30px;top:224px;width:126px"><div class="caption-title">What to watch for</div><div class="small">Flutters or skipping sensation Racing heart beat Lightheaded spells or passing out Trouble breathing</div></div>
      <div class="caption" style="left:160px;top:226px;width:100px"><div class="caption-title">How to Diagnose</div><div class="small">EKG Heart monitor EP study</div></div>
      <div class="caption" style="left:268px;top:226px;width:110px"><div class="caption-title">How to treat</div><div class="small">Medications Lifestyle change Ablation Devices</div></div>
    </div>
    <div class="page right">
      <div class="page-heading" style="top:17px;font-size:21px">More about Arrhythmia</div>
      <div class="heading-rule" style="left:66px;top:44px;width:90px"></div>
      <p class="small" style="position:absolute;left:32px;top:57px;width:332px;text-align:center;font-size:7px;line-height:9px">Arrhythmia refers to an abnormality of the electrical system of the heart. This may result in the heart beating too fast or too slow or irregularly. If the heart is not beating correctly, then the heart may not pump as strong as it should. This can cause symptoms.</p>
      <div class="panel" style="left:17px;top:110px;width:198px;height:145px">
        <div class="panel-title" style="position:absolute;left:12px;top:13px;font-size:9px">Symptoms include things such as</div>
        <div class="symptom" style="top:34px"><span class="dot"></span>Skips or flutters in the chest.</div>
        <div class="symptom" style="top:56px"><span class="dot"></span>Racing heart beat</div>
        <div class="symptom" style="top:79px"><span class="dot"></span>Lightheaded spells</div>
        <div class="symptom" style="top:101px"><span class="dot"></span>Passing out spells</div>
        <div class="symptom" style="top:124px"><span class="dot"></span>Trouble breathing</div>
      </div>
      <div class="photo" role="img" aria-label="Anatomical illustration of the heart, lungs and major vessels" style="left:208px;top:103px;width:163px;height:165px;background:radial-gradient(circle at 50% 55%,#b42a2e 0%,#c9484b 18%,#8fb6dc 40%,#cfe2f3 80%)"></div>
    </div>
  </div>
</section>

<!-- Scene 2 -->
<section class="scene" style="top:757px">
  <div class="abs front-cover">
    <div class="cover-art" role="img" aria-label="Glowing blue digital heart with a heartbeat trace"></div>
    <div class="tag">ARRHYTHMIAS</div>
    <h2 class="cover-title">Harwell Heart<br>and Circulatory<br>Care</h2>
    <div class="cover-rule"></div>
    <div class="cover-web">www.harwellrhythm.com</div>
  </div>
  <div class="abs back-cover">
    <div class="tag">ARRHYTHMIAS</div>
    <div class="contact-title">Contact us</div>
    <div class="contact-rule"></div>
    <div class="contact-row" style="top:221px"><svg><use href="#phone"/></svg>540-318-4971</div>
    <div class="contact-row" style="top:236px"><svg><use href="#globe"/></svg>www.harwellrhythm.com</div>
    <div class="contact-row" style="top:250px"><svg><use href="#pin"/></svg>2945 Pelton Avenue, Suites 300 &amp; 400,<br>Larkfield, VA 22784</div>
  </div>
  <div class="abs spread">
    <div class="page left">
      <div class="page-heading" style="top:14px;font-size:20px">How to diagnose arrhythmias</div>
      <div class="heading-rule" style="left:128px;top:40px;width:100px"></div>
      <div class="item" style="left:28px;top:60px"><svg><use href="#tick"/></svg><div><div class="item-title">EKG:</div><div class="small">Shows the hearts rhythm and electrical pattern at one moment in time</div></div></div>
      <div class="item" style="left:28px;top:84px"><svg><use href="#tick"/></svg><div><div class="item-title">Holter monitor:</div><div class="small">Wear a monitor that records all your heart's electrical activity for 1 to 3 days</div></div></div>
      <div class="item" style="left:28px;top:115px"><svg><use href="#tick"/></svg><div><div class="item-title">Event monitor:</div><div class="small">Wear a monitor for up to a month that records your heart's activity when you push a button</div></div></div>
      <div class="item" style="left:28px;top:146px"><svg><use href="#tick"/></svg><div><div class="item-title">MCOT:</div><div class="small">Wear a monitor that records all your heart's electrical activity for a month</div></div></div>
      <div class="item" style="left:28px;top:172px"><svg><use href="#tick"/></svg><div><div class="item-title">Loop recorder:</div><div class="small">Small implant under the skin that can record all the heart's electrical activity for a few years.</div></div></div>
      <div class="item" style="left:28px;top:201px"><svg><use href="#tick"/></svg><div><div class="item-title">Tilt Table:</div><div class="small">Test where blood pressure and heart rate are recorded as you are slowly raised on a table from flat to nearly upright</div></div></div>
      <div class="item" style="left:28px;top:232px"><svg><use href="#tick"/></svg><div><div class="item-title">EP study:</div><div class="small">Procedure where an electrical specialist places specialized catheters (small tubes the size of coffee straws) into the heart to analyze the heart's electrical system.</div></div></div>
      <div class="photo" role="img" aria-label="Doctor reviewing a sheet of medical scan films" style="left:224px;top:61px;width:154px;height:204px;background:linear-gradient(160deg,#d9e3e6 0%,#24323d 30%,#152028 75%,#c7d3d8 100%)"></div>
    </div>
    <div class="page right">
      <div class="page-heading" style="top:19px;font-size:21px">Treatments</div>
      <div class="heading-rule" style="left:145px;top:47px;width:85px"></div>
      <div class="panel" style="left:17px;top:89px;width:198px;height:146px">
        <div class="panel-title" style="position:absolute;left:17px;top:12px;font-size:11px">Life style changes:</div>
        <div class="life-item" style="top:34px"><svg><use href="#tick"/></svg>Work on ideal weight</div>
        <div class="life-item" style="top:50px"><svg><use href="#tick"/></svg>Control blood pressure</div>
        <div class="life-item" style="top:66px"><svg><use href="#tick"/></svg><span>Avoid stimulants (Coffee, tea, caffeinated beverages, chocolate, over the counter stimulants such as pseudophed)</span></div>
        <div class="life-item" style="top:96px"><svg><use href="#tick"/></svg>Limit alcohol consumption</div>
        <div class="life-item" style="top:111px"><svg><use href="#tick"/></svg>Exercise</div>
        <div class="life-item" style="top:127px"><svg><use href="#tick"/></svg>Treat sleep apnea if present</div>
      </div>
      <div class="photo" role="img" aria-label="Doctor's open hands holding a red heart" style="left:208px;top:75px;width:163px;height:176px;background:radial-gradient(circle at 52% 48%,#d7262b 0%,#d7262b 14%,#e9d6cc 30%,#c6cfd8 65%,#e8eaee 100%)"></div>
    </div>
  </div>
</section>

<!-- Scene 3 -->
<section class="scene" style="top:1531px">
  <div class="abs front-cover">
    <div class="cover-art" role="img" aria-label="Glowing blue digital heart with a heartbeat trace"></div>
    <div class="tag">ARRHYTHMIAS</div>
    <h2 class="cover-title">Harwell Heart<br>and Circulatory<br>Care</h2>
    <div class="cover-rule"></div>
    <div class="cover-web">www.harwellrhythm.com</div>
  </div>
  <div class="abs back-cover">
    <div class="tag">ARRHYTHMIAS</div>
    <div class="contact-title">Contact us</div>
    <div class="contact-rule"></div>
    <div class="contact-row" style="top:221px"><svg><use href="#phone"/></svg>540-318-4971</div>
    <div class="contact-row" style="top:236px"><svg><use href="#globe"/></svg>www.harwellrhythm.com</div>
    <div class="contact-row" style="top:250px"><svg><use href="#pin"/></svg>2945 Pelton Avenue, Suites 300 &amp; 400,<br>Larkfield, VA 22784</div>
  </div>
  <div class="abs spread">
    <div class="page left">
      <div class="page-heading" style="top:17px;font-size:21px">Medications</div>
      <div class="heading-rule" style="left:166px;top:45px;width:74px"></div>
      <div class="item" style="left:28px;top:92px"><svg><use href="#tick"/></svg><div><div class="item-title">Beta blockers:</div><div class="small">Are blood pressure medications that also slow the heart rate down.</div></div></div>
      <div class="item" style="left:28px;top:119px"><svg><use href="#tick"/></svg><div><div class="item-title">Calcium channel blockers:</div><div class="small">Are blood pressure medications that also slow the heart rate down</div></div></div>
      <div class="item" style="left:28px;top:146px"><svg><use href="#tick"/></svg><div><div class="item-title">Digoxin:</div><div class="small">Is a medication that can slow the heart rate</div></div></div>
      <div class="item" style="left:28px;top:174px"><svg><use href="#tick"/></svg><div><div class="item-title">Anti-Arrhythmic:</div><div class="small">Strong medications that work to calm the electrical system of the heart.</div></div></div>
      <div class="item" style="left:28px;top:202px"><svg><use href="#tick"/></svg><div><div class="item-title">Blood thinners:</div><div class="small">May be used with some arrhythmias such as atrial fibrillation to help reduce the risk for stroke.</div></div></div>
      <div class="photo" role="img" aria-label="Hand holding yellow capsules poured from a pill bottle" style="left:228px;top:67px;width:150px;height:185px;background:linear-gradient(160deg,#2a4f8e 0%,#c9d3dc 40%,#e8b49a 65%,#f0a524 85%,#d9c2b0 100%)"></div>
    </div>
    <div class="page right">
      <div class="page-heading" style="top:18px;font-size:21px">Procedure</div>
      <div class="heading-rule" style="left:155px;top:46px;width:74px"></div>
      <div class="panel" style="left:17px;top:104px;width:205px;height:113px">
        <div class="item" style="left:12px;top:16px;width:185px"><svg><use href="#tick"/></svg><div><div class="item-title">Cardioversion:</div><div class="small">The patient is put to sleep and the electrical energy is applied to the body to reset the heart rhythm back to normal.</div></div></div>
        <div class="item" style="left:12px;top:49px;width:185px"><svg><use href="#tick"/></svg><div><div class="item-title">Ablation:</div><div class="small">Electrical specialist takes small tubes called catheters up to the heart to find the abnormal rhythm. They then fix the abnormal rhythm by applying high energy to the problem spot which changes that area so that it not longer causes the problem.</div></div></div>
      </div>
      <div class="photo" role="img" aria-label="Electrophysiology lab equipment in blue light" style="left:222px;top:70px;width:149px;height:182px;background:linear-gradient(160deg,#3d8fd0 0%,#8fc3ea 40%,#f2d9a6 60%,#3c6fb8 100%)"></div>
    </div>
  </div>
</section>
</body>
</html>
```